Velmarine - Mechanic/Collision Center Business Card

We're looking for a business card design for our mechanic/ collision repair shop.

Can be with colours or monochromatic.

See the attached files.

Many thanks

```html
<!DOCTYPE html>
<html lang="pt">
<head>
<meta charset="utf-8">
<title>Velmarine – Business Cards</title>
<link href="https://fonts.googleapis.com/css2?family=Montserrat:wght@700&family=Source+Sans+3:wght@400&display=swap" rel="stylesheet">
<style>
  :root {
    --sheet: #ffffff;
    --card-edge: #222222;
    --band: #121212;
    --accent: #4a8fc4;
    --ink: #111111;
    --mist-top: #ffffff;
    --mist-mid: #eef3f8;
    --mist-bottom: #a9c6de;
    --on-band: #ffffff;
  }
  * { box-sizing: border-box; margin: 0; padding: 0; }
  html, body { width: 1200px; height: 1000px; overflow: hidden; background: var(--sheet); }
  .sheet { position: relative; width: 1200px; height: 1000px; }

  .card {
    position: absolute;
    width: 539px; height: 362px;
    border: 1px solid var(--card-edge);
    background: var(--sheet);
    box-shadow: -3px 3px 5px rgba(0,0,0,0.25);
    overflow: hidden;
    font-family: "Source Sans 3", "Myriad Pro", sans-serif;
    color: var(--ink);
  }
  .card--front-company { left: 33px; top: 98px; }
  .card--front-person  { left: 628px; top: 98px; }
  .card--back-company  { left: 33px; top: 540px; }
  .card--back-person   { left: 628px; top: 540px; }

  .card--centered { text-align: center; }
  .band {
    position: absolute; left: 0; right: 0; top: 117px; height: 27px;
    background: var(--band);
  }
  .brand {
    position: absolute; display: flex; align-items: center; gap: 10px;
    font-family: "Montserrat", sans-serif; font-weight: 700;
    text-transform: uppercase; letter-spacing: 1px; white-space: nowrap;
  }
  .brand__dot { width: 16px; height: 16px; border-radius: 50%; background: var(--accent); flex: none; }
  .card--centered .brand {
    top: 117px; height: 27px; left: 50%; transform: translateX(-50%);
    font-size: 24px; color: var(--on-band);
  }

  .holder {
    font-family: "Montserrat", sans-serif; font-weight: 700;
    color: var(--accent); font-size: 19px; letter-spacing: 0.2px; white-space: nowrap;
  }
  .card--centered .holder { position: absolute; left: 0; right: 0; top: 175px; }
  .card--centered .address { position: absolute; left: 0; right: 0; top: 212px; font-size: 16px; }
  .card--centered .contacts { position: absolute; left: 0; right: 0; top: 244px; font-size: 16px; line-height: 25px; }

  .card--mist {
    background: linear-gradient(to bottom, var(--mist-top) 0%, var(--mist-top) 35%, var(--mist-mid) 70%, var(--mist-bottom) 100%);
    text-align: right;
  }
  .card--mist .holder { position: absolute; right: 42px; top: 47px; }
  .card--mist .brand { left: 42px; top: 150px; font-size: 29px; color: var(--ink); }
  .card--mist .address { position: absolute; right: 42px; top: 149px; font-size: 16px; }
  .card--mist .contacts { position: absolute; right: 42px; top: 247px; font-size: 16px; line-height: 25px; white-space: nowrap; }
</style>
</head>
<body>
<main class="sheet">

  <article class="card card--centered card--front-company">
    <div class="band"></div>
    <div class="brand"><span class="brand__dot"></span>Velmarine</div>
    <h2 class="holder">Velmarine, LDA</h2>
    <p class="address">Rua das Oficinas, 42</p>
    <p class="contacts">+351 210004512 (or just 210004512)<br>1100-318 Lisboa (Postal code)<br>velmarine.mail@oficina.pt&nbsp; ||&nbsp; www.velmarine-oficina.pt</p>
  </article>

  <article class="card card--centered card--front-person">
    <div class="band"></div>
    <div class="brand"><span class="brand__dot"></span>Velmarine</div>
    <h2 class="holder">Duarte Selvinho</h2>
    <p class="address">Rua das Oficinas, 42</p>
    <p class="contacts">+351 910027384 (or just 910027384)<br>1100-318 Lisboa (Postal code)<br>velmarine.mail@oficina.pt&nbsp; ||&nbsp; www.velmarine-oficina.pt</p>
  </article>

  <article class="card card--mist card--back-company">
    <h2 class="holder">Velmarine, LDA</h2>
    <div class="brand"><span class="brand__dot"></span>Velmarine</div>
    <p class="address">Rua das Oficinas, 42</p>
    <p class="contacts">+351 210004512 (or just 210004512)<br>1100-318 Lisboa (Postal code) || velmarine.mail@oficina.pt<br>www.velmarine-oficina.pt</p>
  </article>

  <article class="card card--mist card--back-person">
    <h2 class="holder">Duarte Selvinho</h2>
    <div class="brand"><span class="brand__dot"></span>Velmarine</div>
    <p class="address">Rua das Oficinas, 42</p>
    <p class="contacts">+351 910027384 (or just 910027384)<br>1100-318 Lisboa (Postal code) || velmarine.mail@oficina.pt<br>www.velmarine-oficina.pt</p>
  </article>

</main>
</body>
</html>
```